Flyer - Crestline Dental Marbury

** Please do not use my words - word-for-word on the flyer design **
We have recently bought an established dental business. However we are not getting new customers through the door. We plan to implement aggressive local marketing strategies including flyer distribution. We are looking for an eye-catching must read flyer design. Some details & content ideas are as below.
1. A5 size - Double Sided
2. Our business name is Crestline Dental Marbury. Logo is attached. Website is www.crestlinedentalmarbury.com.au where lot of useful information can be found.
3. Practice has a long & proud history serving "Lower North Shore" since 1958. We provide quality dental care at affordable prices.
4. List of services can be found on website
5. Perhaps a snippet of Orbisa Map Location would be useful. Also the fact that 3-hour free parking is available in Fernleigh Arcade less than 100m away from practice. Plenty of 2-hours street parking is available too.
6. Opening hours can be found on website. Fact that we are open on Saturdays and till late on Tuesdays is worth calling out.
7. We would like to run a campaign of offers with this flyer. Give it a name! Details below.
a) NO GAP Checkup and Clean with any major Private Health Fund. Includes oral exam, 2 X-Rays, Scale & Polish and Fluoride Treatment
b) Genuine Teeth Whitening for $199 (usually $399 save $200)
c) 10% off on all major dental. Includes fillings, crowns, bridges and root canal treatment
8. We are KELMA Preferred Provider means KELMA members get maximum benefit. KELMA Patron Plus logo attached.
9. We participate in Office of Ranger Welfare Fee Schedule. Logo attached.
10. Call out WE ACCEPT ALL HEALTH FUNDS
Dental
- Helvetica Neue, Myriad Pro

```html
<!DOCTYPE html>
<html lang="en">
<head>
<meta charset="utf-8">
<title>Crestline Dental Marbury – Flyer</title>
<link rel="stylesheet" href="https://fonts.googleapis.com/css2?family=Source+Sans+3:wght@400;600;700&display=swap">
<style>
  :root {
    --lime: #a6c83a;
    --teal: #5cbf9c;
    --teal-pale: #dff2ea;
    --ink: #1a1a1a;
    --map-base: #e6e2d8;
    --map-green: #cfe0c3;
    --paper: #ffffff;
  }
  * { margin: 0; padding: 0; box-sizing: border-box; }
  html, body { width: 1200px; height: 1000px; overflow: hidden; background: var(--paper); }
  body { font-family: "Source Sans 3", "Helvetica Neue", Arial, sans-serif; color: var(--ink); position: relative; }
  .flyer { position: absolute; left: 248px; top: 0; width: 704px; height: 1000px; border-left: 1px solid #333; }
  .pattern-band { position: absolute; left: 14px; width: 690px; height: 72px; border-radius: 12px;
    background: linear-gradient(90deg, var(--teal-pale), #c9ebde, var(--teal-pale)); }
  .pattern-band.top { top: 16px; }
  .pattern-band.bottom { top: 914px; }
  .abs { position: absolute; }
  .nowrap { white-space: nowrap; }
  .heading-lime { color: var(--lime); font-weight: 700; text-transform: uppercase; }
  .heading-teal { color: var(--teal); font-weight: 700; font-size: 20px; }
  .funds { left: 40px; top: 125px; width: 350px; text-align: center; font-size: 19.5px; line-height: 24.5px; }
  .funds .heading-lime { font-size: 20.5px; line-height: 28px; }
  .offer-box { left: 444px; top: 103px; width: 218px; height: 187px; border: 2px solid var(--lime);
    text-align: center; font-size: 19.5px; line-height: 24.3px; padding-top: 3px; white-space: nowrap; }
  .body-text { font-size: 20px; line-height: 24.5px; }
  .benefit { left: 48px; top: 302px; width: 640px; }
  .benefit .heading-lime { text-align: center; display: block; font-size: 19px; line-height: 24px; margin-left: -30px; }
  .contact { left: 48px; top: 411px; width: 640px; }
  .contact .center { text-align: center; margin-left: -24px; }
  .address { color: var(--teal); font-weight: 700; font-size: 26px; line-height: 32px; text-align: center; margin-left: -24px; }
  .parking { margin-top: 14px; }
  .hours { left: 48px; top: 652px; font-size: 20px; line-height: 24.5px; }
  .hours .label { color: var(--lime); font-weight: 700; }
  .map { left: 387px; top: 622px; width: 257px; height: 169px;
    background: linear-gradient(135deg, var(--map-base) 0%, var(--map-green) 50%, var(--map-base) 100%); }
  .call { left: 20px; top: 815px; width: 640px; text-align: center; }
  .phone { color: var(--teal); font-weight: 700; font-size: 27px; line-height: 32px; }
  .book { font-size: 20px; }
</style>
</head>
<body>
  <main class="flyer">
    <div class="pattern-band top" role="img" aria-label="Row of decorative tooth outlines"></div>

    <section class="funds abs">
      <p class="heading-lime nowrap">We accept all health fund cards!</p>
      <p>KELMA &amp; NORVA</p>
      <p>RANGER WELFARE</p>
      <p>ELDERS PASS</p>
      <p>CLAIMPOINT</p>
    </section>

    <aside class="offer-box abs">
      NO GAP Checkup and<br>Clean with any major<br>Private Health Fund.<br>Includes<br>oral exam, 2 X-Rays,<br>Scale &amp; Polish and<br>Fluoride Treatment
    </aside>

    <section class="benefit abs body-text">
      <span class="heading-lime">The Young Smiles Benefit Plan</span>
      <p class="nowrap">Paid by Carelink, provides access to benefits for basic dental services for<br>eligible children.&nbsp; You can confirm your child’s eligibility by calling Care-<br>link on 139 240.</p>
    </section>

    <section class="contact abs body-text">
      <p class="heading-teal center">CONTACT US</p>
      <p class="address">118 Harbour Avenue Marbury NSW 2091</p>
      <p class="nowrap">We are located 100m from Fernleigh Arcade, and directly opposite<br>Civic Service Hub and Pebble Lane Café on the intersection of Harbour<br>Avenue and Bramble Street.</p>
      <p class="parking nowrap">Fernleigh Arcade with over 2500 car spaces offers convenient 3-hours<br>free parking and there is also ample 2-hours street parking available.</p>
    </section>

    <section class="hours abs">
      <p><span class="label">Office Hours</span>:</p>
      <p>Monday 8:30am – 5:30pm</p>
      <p>Tuesday 12:00pm – 8:00pm</p>
      <p>Wednesday – Friday 8:30am – 5:30pm</p>
      <p>Saturday 9:00am – 4:00pm</p>
    </section>

    <div class="map abs" role="img" aria-label="Orbisa Map street map showing the practice location"></div>

    <section class="call abs">
      <p class="heading-teal">Call us on</p>
      <p class="phone">(02) 5550 1842</p>
      <p class="book">to book an appointment now!</p>
    </section>

    <div class="pattern-band bottom" role="img" aria-label="Row of decorative tooth outlines"></div>
  </main>
</body>
</html>
```